依頼詳細
【サイトの最大の要望】
・ターゲットに合った分かりやすいデザイン

【強み】
・整体と美容の両方からお客様の身体の不調やなりたい自分に合った施術を行える点です。

【おすすめメニュー】
・お客様の身体の不調や気になる部分に合わせたオーダーメイドの施術

【ターゲット】
・30代・40代の会社員、自営、パートなど自分にかけるお金がある人。

【デザインについて】
・部分的に参考サイトのようなフレームを使用していただきたいです。
・参考サイトの「お知らせ」の背景で使用しているような
お花などのボタニカルなイラストなど入れてほしいです。

【参考サイト】
・tonsor HALVEN MOREL(トンソル ハルヴェン モレル)
http://morel-tonsor.example/
白を基調としている点や、上品なゴールドのフォント、「お知らせ」の背景で使用している
お花のイラストをアクセントで使用しているところが気に入っています。

http://quillmere-works.example/
とても見やすくて分かりやすくていいなと思っています。

http://vesna-lumio.example/
フレームや両隅の装飾が好きです。

http://kp-dermaluxe.example/
色合いやテクスチャー、お花のイラストなどが女性らしい雰囲気でイメージに一番近いです。

【サイトマップ】
①TOP
② アクセス
③初めての方へ
④プロフィール
⑤ 当サロンの特徴
⑥身体の外側の不調(痛み・しびれ)
⑦身体の内側の不調(内臓などの不調・冷え症・アトピー)
⑧ストレス
⑨顔に関するお悩み
⑩体に関するお悩み
⑪リラクゼーション
⑫お客様の声
⑬キャンペーン、特典
⑭セミナー・スクールのご案内
⑮料金
⑯ニュース(一覧)
∟⑰ニュース(詳細)
⑱ブログ(一覧)
∟⑲ブログ(詳細)
⑳予約、お問い合わせ、プライバシー・ポリシー

■TOPページにGメニューとは別にデザインの入り口を必須で設けて頂きたいコンテンツは以下となります。
(それ以外のページに関してはランサーにお任せします)

タイトル:メニュー
⑥身体の外側の不調(痛み・しびれ)
⑧ストレス
⑨顔に関するお悩み
⑩体に関するお悩み
⑪リラクゼーション

⑫お客様の声
⑬キャンペーン、特典
⑰ニュース(詳細)
⑲ブログ(詳細)

下記のボタンもしくはバナー希望です。
・予約
・お問い合わせ
・キャンペーン
サイトURL
https://trelvane.sitebloomer.example/
ページ数
1ページ
希望イメージ
シンプル 複雑
単色 カラフル
暗い 明るい
日常 高級
遊び心 厳粛
未来的 伝統的
女性的 男性的
希望する色
緑系、ゴールド
納品ファイル
• イラストレーター形式 (.ai)
• フォトショップ形式 (.psd)
• PNG形式 (.png)
補足説明
【店舗へのご連絡はおやめください】
ワークリンク規約にもありますが、店舗への通常業務に支障が出るため、
直接電話等のお問い合わせをお控え頂きますよう、ご協力願います。

【素材写真】
下記よりダウンロードしてご使用ください。
https://3.filedrift.example/0225-k81937b52c904f6a13bd7e2059c771b3
TOPイメージを添付しましたので、延長を希望いたします。

下記よりダウンロードしてご参照ください。
https://20.filedrift.example/0131-p47390a81be527c09d6f1a38e4b92c05

ご多忙のところ恐縮ですが、宜しくお願いいたします。
テキストや画像などのダミーは無い状態でご提案をお願いいたします。

全体的にバランスが良く、整体っぽくないメインビジュアルが特に良かったです。

たくさんのご提案、ありがとうございました。
どのデザインも素敵で選定が難しかったです。

また、何か機会がありましたら、宜しくお願いいたします。

```html
<!DOCTYPE html>
<html lang="ja">
<head>
<meta charset="utf-8">
<title>TRELVANE</title>
<link rel="stylesheet" href="https://fonts.googleapis.com/css2?family=Cinzel:wght@400;600&family=Noto+Serif+JP:wght@400;600&display=swap">
<style>
:root{
  --gold:#b48f55;
  --gold-dark:#8f6c39;
  --ink:#4a3f38;
  --white:#ffffff;
  --pink:#c8668f;
  --pink-soft:#f6dfe4;
  --pink-btn:#ec9db0;
  --blue:#1f5d9c;
  --dark:#3d3733;
}
*{margin:0;padding:0;box-sizing:border-box}
html,body{width:1200px;height:3796px;overflow:hidden}
body{font-family:"Noto Serif JP",serif;color:var(--ink);background:var(--white);position:relative}
section,header,footer{position:absolute;left:0;width:1200px}

/* header */
.site-header{top:0;height:88px;background:var(--white);border-bottom:1px solid #eee}
.brand{position:absolute;left:28px;top:22px;font-family:"Cinzel",serif;font-size:30px;font-weight:600;color:var(--gold);letter-spacing:2px}
.gnav{position:absolute;left:380px;top:48px;display:flex;font-size:15px;color:var(--ink)}
.gnav span{padding:0 24px;border-left:1px solid #c9b89c;font-family:"Cinzel",serif}
.gnav span:first-child{border-left:none}
.top-btns{position:absolute;right:20px;top:6px;display:flex;gap:6px}
.top-btns span{display:block;width:90px;height:26px;line-height:26px;text-align:center;font-size:11px;color:var(--white)}
.tb-camp{background:var(--gold)}
.tb-res{background:#6f655c}
.tb-contact{background:var(--pink-btn)}

/* hero */
.hero{top:88px;height:512px}
.hero-photo{position:absolute;inset:0;background:linear-gradient(90deg,#e9e2dc 0%,#d8c9bf 35%,#a64f4f 60%,#8a3c43 80%,#b4767a 100%)}
.hero-copy{position:absolute;right:70px;top:70px;font-size:46px;line-height:1.5;color:var(--white);font-weight:600;letter-spacing:4px;text-shadow:0 2px 8px rgba(0,0,0,.35)}
.hero-copy span{display:block}
.hero-copy span:last-child{padding-left:30px}

/* concept */
.concept{top:600px;height:560px;background:var(--white)}
.concept-photo{position:absolute;right:0;top:0;width:560px;height:560px;background:linear-gradient(90deg,rgba(255,255,255,1) 0%,rgba(243,238,233,.8) 50%,#ebe4dc 100%)}
.concept-frame{position:absolute;left:390px;top:30px;width:420px;height:420px}
.concept-body{position:absolute;left:470px;top:160px;width:260px;text-align:center}
.concept-body h2{font-family:"Cinzel",serif;font-weight:400;color:var(--gold);font-size:28px;margin-bottom:12px}
.concept-body p{font-size:13px;line-height:1.9;color:var(--gold-dark)}
.concept-more{position:absolute;left:555px;top:318px;width:90px;font-size:12px;text-align:center;color:var(--gold);border-bottom:1px solid var(--gold);padding-bottom:4px;font-family:"Cinzel",serif}

/* menu */
.menu{top:1160px;height:520px;background:linear-gradient(180deg,#54504c 0%,#3f3935 100%)}
.menu-photo{position:absolute;inset:0;background:linear-gradient(90deg,rgba(120,60,70,.35),rgba(60,55,50,.2) 60%,rgba(90,80,70,.3))}
.sec-title{position:absolute;left:0;width:1200px;text-align:center}
.sec-title h2{font-family:"Cinzel",serif;font-weight:400;font-size:30px;letter-spacing:3px}
.sec-title small{display:block;font-size:11px;margin-top:2px}
.menu .sec-title{top:36px;color:var(--white)}
.menu-grid{position:absolute;left:170px;top:130px;display:grid;grid-template-columns:repeat(3,200px);column-gap:90px;row-gap:30px}
.menu-item{height:88px;background:var(--white);text-align:center;padding-top:20px;position:relative}
.menu-item::after{content:"";position:absolute;right:10px;bottom:10px;width:8px;height:8px;border-right:1px solid var(--gold);border-bottom:1px solid var(--gold);transform:rotate(-45deg)}
.menu-item b{display:block;font-weight:400;font-size:17px;color:var(--gold-dark);letter-spacing:3px}
.menu-item small{font-family:"Cinzel",serif;font-size:10px;color:var(--gold)}

/* profile / beginner */
.intro{top:1680px;height:720px;background-color:#fbeef0;background-image:radial-gradient(#f0c9d1 1.5px,transparent 1.6px);background-size:14px 14px}
.card{position:absolute;top:100px;width:400px;height:540px;color:var(--white)}
.card-profile{left:170px;background:var(--pink)}
.card-beginner{left:630px;background:var(--blue)}
.card-photo{height:200px}
.card-profile .card-photo{background:linear-gradient(180deg,#f4f1ee,#dcd3cb)}
.card-beginner .card-photo{background:linear-gradient(135deg,#f2d6a9,#e9a5b4 50%,#9fc3d9)}
.card h3{font-family:"Cinzel",serif;font-weight:400;text-align:center;font-size:24px;margin-top:26px}
.card h3 small{display:block;font-family:"Noto Serif JP",serif;font-size:10px}
.card-text{padding:18px 40px 0;font-size:11.5px;line-height:1.9}
.card-text .name{font-size:18px;display:block;margin-bottom:4px}
.card-more{position:absolute;left:120px;bottom:28px;width:160px;height:36px;line-height:36px;background:var(--white);text-align:center;font-size:13px;font-family:"Cinzel",serif}
.card-profile .card-more{color:var(--pink)}
.card-beginner .card-more{color:var(--blue)}
.card-beginner .card-text{padding-top:24px}

/* voice */
.voice{top:2400px;height:460px;background:linear-gradient(180deg,#e8e7e6,#cfcdcb 60%,#dcdad8)}
.voice .sec-title{top:40px;color:var(--ink)}
.voice-list{position:absolute;left:130px;top:120px;display:flex;gap:70px}
.voice-card{width:260px;height:150px;background:var(--white);display:flex;padding:14px;gap:14px;box-shadow:0 2px 6px rgba(0,0,0,.1)}
.voice-img{width:110px;height:122px;background:linear-gradient(180deg,#eef2f7,#c7d3e2)}
.voice-txt{font-size:12px;line-height:1.8;color:var(--ink)}
.voice-txt b{display:block;font-weight:400;font-size:14px;margin-bottom:6px;color:var(--gold-dark)}
.voice-more{position:absolute;left:530px;top:335px;width:140px;height:36px;line-height:36px;background:var(--gold);color:var(--white);text-align:center;font-size:13px;font-family:"Cinzel",serif}

/* news */
.news{top:2860px;height:420px;background:var(--pink-soft)}
.news-head{position:absolute;left:120px;top:58px;display:flex;align-items:baseline;gap:10px;color:var(--gold-dark)}
.news-head h2{font-family:"Cinzel",serif;font-weight:400;font-size:26px}
.news-head small{font-size:11px}
.news-list{position:absolute;left:120px;top:120px;width:420px;list-style:none}
.news-list li{display:flex;gap:26px;font-size:15px;height:60px;align-items:center;border-bottom:1px solid #e8bfc7}
.news-list time{color:var(--ink)}
.news-list span{color:var(--gold-dark);text-decoration:underline}
.banner{position:absolute;left:690px;width:400px;height:84px;border-radius:14px;text-align:center;line-height:84px;font-family:"Cinzel",serif;font-size:28px;letter-spacing:2px}
.banner-blog{top:100px;background:var(--pink-btn);color:var(--white)}
.banner-camp{top:220px;background:var(--white);color:var(--pink-btn)}

/* contact */
.contact{top:3280px;height:340px;background:linear-gradient(180deg,#4a4542,#6b625d 50%,#3f3a37)}
.contact-overlay{position:absolute;left:140px;top:0;width:920px;height:340px;background:rgba(255,255,255,.72)}
.contact .sec-title{top:36px;color:var(--gold-dark)}
.contact-text{position:absolute;left:0;top:120px;width:1200px;text-align:center;font-size:12.5px;line-height:1.9}
.contact-btns{position:absolute;left:190px;top:210px;display:flex;gap:60px}
.contact-btns span{display:block;width:220px;height:46px;line-height:46px;background:#6b4a36;color:var(--white);text-align:center;font-size:14px;letter-spacing:2px}

/* footer */
.site-footer{top:3620px;height:176px;background:var(--white)}
.site-footer .brand{left:28px;top:40px}
.site-footer .gnav{top:110px;left:150px}
</style>
</head>
<body>

<header class="site-header">
  <div class="brand">TRELVANE</div>
  <nav class="gnav"><span>TOP</span><span>CONCEPT</span><span>BEGINNER</span><span>ABOUT</span><span>ACCESS</span><span>NEWS</span></nav>
  <div class="top-btns"><span class="tb-camp">キャンペーン</span><span class="tb-res">ご予約</span><span class="tb-contact">お問い合わせ</span></div>
</header>

<section class="hero">
  <div class="hero-photo" role="img" aria-label="施術風景の写真と装飾タペストリー"></div>
  <h1 class="hero-copy"><span>身体のなかが整う</span><span>だから綺麗になる</span></h1>
</section>

<section class="concept">
  <div class="concept-photo" role="img" aria-label="サロン店内の写真"></div>
  <svg class="concept-frame" viewBox="0 0 420 420" aria-hidden="true">
    <g fill="none" stroke="#b48f55" stroke-width="2">
      <polygon points="210,20 400,210 210,400 20,210"/>
      <polygon points="210,34 386,210 210,386 34,210" stroke-width="1"/>
      <rect x="62" y="110" width="296" height="210" fill="rgba(255,255,255,.85)" stroke-width="1"/>
    </g>
  </svg>
  <div class="concept-body">
    <h2>CONCEPT</h2>
    <p>当店の施術での根源することは<br>「どんな時代も、どんな場面も<br>綺麗を信じてほしい」です</p>
  </div>
  <div class="concept-more">MORE</div>
</section>

<section class="menu">
  <div class="menu-photo" role="img" aria-label="施術ベッドのある店内写真"></div>
  <div class="sec-title"><h2>MENU</h2><small>メニュー</small></div>
  <div class="menu-grid">
    <div class="menu-item"><b>メニュー</b><small>MENU</small></div>
    <div class="menu-item"><b>メニュー</b><small>MENU</small></div>
    <div class="menu-item"><b>メニュー</b><small>MENU</small></div>
    <div class="menu-item"><b>メニュー</b><small>MENU</small></div>
    <div class="menu-item"><b>メニュー</b><small>MENU</small></div>
    <div class="menu-item"><b>メニュー</b><small>MENU</small></div>
    <div class="menu-item"><b>メニュー</b><small>MENU</small></div>
    <div class="menu-item"><b>メニュー</b><small>MENU</small></div>
    <div class="menu-item"><b>メニュー</b><small>MENU</small></div>
  </div>
</section>

<section class="intro">
  <article class="card card-profile">
    <div class="card-photo" role="img" aria-label="施術者のプロフィール写真"></div>
    <h3>PROFILE<small>プロフィール</small></h3>
    <div class="card-text">
      <span class="name">水野 千景</span>
      整体師・美容施術者として十年以上<br>
      身体と肌の両面から施術を担当<br>
      各種講座の講師としても活動中<br>
      資格：整体師／美容技術者 ほか
    </div>
    <div class="card-more">MORE</div>
  </article>

  <article class="card card-beginner">
    <div class="card-photo" role="img" aria-label="店内のウェルカムボードの写真"></div>
    <h3>BEGINNER<small>初めての方へ</small></h3>
    <div class="card-text">
      初めてご来店の方へ、施術の流れやご予約方法をご案内します。
      カウンセリングでお身体の状態やお悩みを伺い、一人ひとりに合わせた施術をご提案いたします。
      お気軽にご相談ください。
    </div>
    <div class="card-more">MORE</div>
  </article>
</section>

<section class="voice">
  <div class="sec-title"><h2>VOICE</h2><small>お客様の声</small></div>
  <div class="voice-list">
    <div class="voice-card"><div class="voice-img" role="img" aria-label="お客様アンケート用紙の写真"></div><div class="voice-txt"><b>Aさん</b>ここにテキストが<br>入ります ここに<br>テキストが入ります</div></div>
    <div class="voice-card"><div class="voice-img" role="img" aria-label="お客様アンケート用紙の写真"></div><div class="voice-txt"><b>Bさん</b>ここにテキストが<br>入ります ここに<br>テキストが入ります</div></div>
    <div class="voice-card"><div class="voice-img" role="img" aria-label="お客様アンケート用紙の写真"></div><div class="voice-txt"><b>Cさん</b>ここにテキストが<br>入ります ここに<br>テキストが入ります</div></div>
  </div>
  <div class="voice-more">MORE</div>
</section>

<section class="news">
  <div class="news-head"><h2>NEWS</h2><small>ニュース</small></div>
  <ul class="news-list">
    <li><time>2020/01/01</time><span>ここにテキストが入ります</span></li>
    <li><time>2020/01/01</time><span>ここにテキストが入ります</span></li>
    <li><time>2020/01/01</time><span>ここにテキストが入ります</span></li>
    <li><time>2020/01/01</time><span>ここにテキストが入ります</span></li>
  </ul>
  <div class="banner banner-blog">BLOG</div>
  <div class="banner banner-camp">CAMPAIGN</div>
</section>

<section class="contact">
  <div class="contact-overlay" role="img" aria-label="花の写真を背景にした淡い帯"></div>
  <div class="sec-title"><h2>CONTACT</h2><small>お問い合わせ</small></div>
  <p class="contact-text">ご予約やお問い合わせはこちらから。<br>お気軽にご連絡ください。</p>
  <div class="contact-btns"><span>ご予約</span><span>お問い合わせ</span><span>アクセス</span></div>
</section>

<footer class="site-footer">
  <div class="brand">TRELVANE</div>
  <nav class="gnav"><span>TOP</span><span>CONCEPT</span><span>BEGINNER</span><span>ABOUT</span><span>ACCESS</span><span>NEWS</span></nav>
</footer>

</body>
</html>
```